Flyer for Car Detailing Shop

I am opening a detailing shop. I am looking for a nice, easy to read single sided flyer I can hand out at car shows, hang in store windows and to my clients and customers to promote my business. I want it a little professional yet attention grabbing. I want someone to look at it and go "holy shit, thats a nice flyer" haha

Here are some things that must be included:
- Company Name: Brightfern Motorworks Detailing & Coatings
- Tag Line: The Science of Detailing
- Address: 4150 Harlow Rd, Linden Falls, 48190
- www.brightfernmotor.example
- Find Us on social Media! ::insert facebook and instagram logo
Colors: Black, Lime Green and Purple for accents, etc

HAND WASH
- Express Wash start at $25
- Deluxe Wash Start at $50

EXTERIOR DETAILING
-Basic Packages Start at $160
- Deluxe Packages Start at $350

INTERIOR DETAILING
- Basic Packages Start at $60
- Deluxe Packages Start at $200

New Car Prep and Ceramic Coatings
*Consultation required prior to beginning work*
- Paint: Starting at $500
- Interior: Starting at $100
- Wheels Off: Starting at $200
- Trim: Starting at $100
- Windows: $50 windshield/ $25 per pane

Additional Services
- Scratch removal
- Ozone Treatment
- Headlight Restoration
- Chip Repair

```html
<!DOCTYPE html>
<html lang="en">
<head>
<meta charset="utf-8">
<title>Brightfern Motorworks – The Science of Detailing</title>
<link rel="stylesheet" href="https://fonts.googleapis.com/css2?family=Poppins:wght@400;500;600;700;800&display=swap">
<style>
  :root{
    --backdrop:#4b403e;
    --lime:#6abf4f;
    --lime-dark:#5cb044;
    --purple:#7b1d82;
    --purple-row:#8c3a91;
    --ink:#1f1f1f;
    --band-dark:#2e2e2f;
    --charcoal:#333335;
    --white:#ffffff;
    --text-grey:#4a4a4a;
  }
  *{margin:0;padding:0;box-sizing:border-box}
  html,body{width:1200px;height:2371px;overflow:hidden;background:var(--backdrop);font-family:'Poppins',sans-serif}
  .flyer{position:absolute;left:51px;top:475px;width:1056px;height:1365px;background:var(--white);transform:scale(1.04);transform-origin:top left;overflow:hidden;box-shadow:0 20px 40px rgba(0,0,0,.35)}
  .hero-photo{position:absolute;left:0;top:0;width:1056px;height:693px;background:linear-gradient(100deg,#ffffff 0%,#f4f2ea 25%,#d8d6d2 45%,#b9bcc0 70%,#8f959b 100%)}
  .brand-mark{position:absolute;left:159px;top:120px;width:72px;height:72px;border-radius:50%;background:var(--ink)}
  .brand-name{position:absolute;left:30px;top:225px;width:330px;text-align:center;font-weight:800;font-size:40px;line-height:1.1;color:var(--ink);letter-spacing:.5px}
  .shapes{position:absolute;left:0;top:0}
  .tagline{position:absolute;left:125px;top:470px;font-weight:800;line-height:1}
  .tagline .the{display:block;margin-left:205px;font-weight:400;font-size:50px;color:var(--white)}
  .tagline .science{display:block;font-size:66px;color:var(--lime);margin-top:6px}
  .tagline .of{font-weight:400;font-size:44px;color:var(--white)}
  .tagline .detailing{font-size:66px;color:var(--lime)}
  .extras{position:absolute;left:675px;top:465px;color:var(--white)}
  .extras h2{font-size:30px;font-weight:500;color:var(--ink);letter-spacing:.3px}
  .extras h2 b{font-weight:700}
  .extras ul{list-style:none;margin:6px 0 0 50px}
  .extras li{font-size:25px;line-height:38px;display:flex;align-items:center;gap:14px}
  .extras li svg{width:18px;height:18px}
  .services{position:absolute;left:8px;top:765px;display:flex;gap:5px}
  .service{width:343px;position:relative;box-shadow:0 12px 14px -8px rgba(0,0,0,.45)}
  .service .icon{position:absolute;left:50%;top:-52px;transform:translateX(-50%);width:78px;height:78px;border-radius:50%;border:4px solid var(--white);display:flex;align-items:center;justify-content:center}
  .service h3{height:75px;display:flex;align-items:center;justify-content:center;font-size:23px;font-weight:700;color:var(--white);padding-top:20px}
  .service .row{height:76px;display:flex;flex-direction:column;justify-content:center;text-align:center;color:var(--white);font-size:19px;line-height:1.25;border-top:2px solid rgba(255,255,255,.35)}
  .service .row b{font-weight:700}
  .hand-wash .icon,.hand-wash h3{background:var(--lime-dark)}
  .hand-wash .row{background:var(--lime)}
  .exterior .icon,.exterior h3{background:var(--purple)}
  .exterior .row{background:var(--purple-row)}
  .interior .icon,.interior h3{background:var(--ink)}
  .interior .row{background:var(--charcoal)}
  .coatings-rule{position:absolute;left:0;top:1035px;width:1056px;height:3px;background:var(--lime)}
  .coatings-ribbon{position:absolute;left:264px;top:1037px;width:528px;height:40px;background:var(--lime);clip-path:polygon(0 0,100% 0,95% 100%,5% 100%);color:var(--white);font-weight:700;font-size:23px;display:flex;align-items:center;justify-content:center}
  .consult-note{position:absolute;left:0;top:1085px;width:1056px;text-align:center;font-size:20px;color:var(--text-grey)}
  .coatings{position:absolute;left:14px;top:1128px;display:flex;gap:13px}
  .coating{width:195px;height:81px;background:var(--charcoal);color:var(--white);text-align:center}
  .coating h4{height:30px;background:var(--purple);font-size:19px;font-weight:700;line-height:30px}
  .coating p{font-size:20px;font-weight:500;line-height:46px}
  .coating p.stacked{line-height:1;padding-top:9px}
  .coating p.stacked small{display:block;font-size:14px;font-weight:400}
  .social-label{position:absolute;left:35px;top:1292px;font-weight:600;font-size:23px;line-height:1.15;color:var(--lime)}
  .social-icons{position:absolute;left:225px;top:1292px;display:flex;gap:14px}
  .social-icons span{width:50px;height:50px;border:4px solid var(--white);border-radius:10px}
  .contact{position:absolute;right:36px;top:1265px;text-align:right;color:var(--white);font-style:normal}
  .contact .address{font-size:23px}
  .contact .web{font-size:31px;line-height:1.2}
  .contact .web b{font-weight:700}
</style>
</head>
<body>
<main class="flyer">
  <div class="hero-photo" role="img" aria-label="Photo of a silver SUV being rinsed with a pressure washer in sunlight"></div>
  <div class="brand-mark"></div>
  <div class="brand-name">Brightfern Motorworks</div>

  <svg class="shapes" width="1056" height="1365" viewBox="0 0 1056 1365" aria-hidden="true">
    <polygon points="0,693 1056,693 1056,765 0,765" fill="#ffffff"/>
    <polygon points="0,440 450,440 703,693 85,693 40,640 0,640" fill="#2e2e2f"/>
    <polygon points="0,640 40,640 85,693 0,778" fill="#6abf4f"/>
    <polygon points="640,440 1056,440 1056,693 695,693 552,590" fill="#6abf4f"/>
    <polygon points="0,1268 545,1268 450,1365 0,1365" fill="#333335"/>
    <polygon points="432,1245 1056,1245 1056,1356 455,1356 545,1268 432,1268" fill="#6abf4f"/>
  </svg>

  <h1 class="tagline">
    <span class="the">THE</span>
    <span class="science">SCIENCE</span>
    <span class="of">OF</span> <span class="detailing">DETAILING</span>
  </h1>

  <section class="extras">
    <h2>ADDITIONAL <b>SERVICES</b></h2>
    <ul>
      <li><svg viewBox="0 0 18 18"><circle cx="9" cy="9" r="9" fill="#2e2e2f"/><path d="M5 9.2l2.6 2.6L13 6.4" stroke="#6abf4f" stroke-width="2.4" fill="none"/></svg>Chip Repair</li>
      <li><svg viewBox="0 0 18 18"><circle cx="9" cy="9" r="9" fill="#2e2e2f"/><path d="M5 9.2l2.6 2.6L13 6.4" stroke="#6abf4f" stroke-width="2.4" fill="none"/></svg>Headlight Restoration</li>
      <li><svg viewBox="0 0 18 18"><circle cx="9" cy="9" r="9" fill="#2e2e2f"/><path d="M5 9.2l2.6 2.6L13 6.4" stroke="#6abf4f" stroke-width="2.4" fill="none"/></svg>Ozone Treatment</li>
      <li><svg viewBox="0 0 18 18"><circle cx="9" cy="9" r="9" fill="#2e2e2f"/><path d="M5 9.2l2.6 2.6L13 6.4" stroke="#6abf4f" stroke-width="2.4" fill="none"/></svg>Scratch removal</li>
    </ul>
  </section>

  <section class="services">
    <article class="service hand-wash">
      <div class="icon"><svg width="40" height="40" viewBox="0 0 40 40"><rect x="8" y="8" width="24" height="24" rx="4" fill="none" stroke="#fff" stroke-width="2.5"/></svg></div>
      <h3>HAND WASH</h3>
      <div class="row">Express Wash start<b>AT $25</b></div>
      <div class="row">Deluxe Wash Start<b>AT $50</b></div>
    </article>
    <article class="service exterior">
      <div class="icon"><svg width="44" height="34" viewBox="0 0 44 34"><path d="M6 18l5-10h22l5 10v10H6z" fill="none" stroke="#fff" stroke-width="2.5"/><circle cx="13" cy="22" r="2.5" fill="#fff"/><circle cx="31" cy="22" r="2.5" fill="#fff"/></svg></div>
      <h3>EXTERIOR DETAILING</h3>
      <div class="row">Basic Packages Start<b>AT $160</b></div>
      <div class="row">Deluxe Packages Start<b>AT $350</b></div>
    </article>
    <article class="service interior">
      <div class="icon"><svg width="44" height="44" viewBox="0 0 44 44"><circle cx="22" cy="22" r="17" fill="none" stroke="#fff" stroke-width="3"/><circle cx="22" cy="22" r="10" fill="none" stroke="#fff" stroke-width="3"/><circle cx="22" cy="22" r="3" fill="#fff"/></svg></div>
      <h3>INTERIOR DETAILING</h3>
      <div class="row">Basic Packages Start<b>AT $60</b></div>
      <div class="row">Deluxe Packages Start<b>AT $200</b></div>
    </article>
  </section>

  <div class="coatings-rule"></div>
  <h2 class="coatings-ribbon">New Car Prep and Ceramic Coatings</h2>
  <p class="consult-note">Consultation required prior to beginning work</p>

  <section class="coatings">
    <div class="coating"><h4>PAINT</h4><p>Starting at $500</p></div>
    <div class="coating"><h4>INTERIOR</h4><p>Starting at $100</p></div>
    <div class="coating"><h4>WHEELS OFF</h4><p>Starting at $200</p></div>
    <div class="coating"><h4>TRIM</h4><p>Starting at $100</p></div>
    <div class="coating"><h4>WINDOWS</h4><p class="stacked">$50 windshield/<small>$25 per pane</small></p></div>
  </section>

  <p class="social-label">Find Us on<br>social Media!</p>
  <div class="social-icons" aria-hidden="true"><span></span><span></span></div>

  <address class="contact">
    <div class="address">4150 Harlow Rd, Linden Falls, 48190</div>
    <div class="web">www.<b>brightfernmotor</b>.example</div>
  </address>
</main>
</body>
</html>
```